Business Card for beauty technology startup

Design Glowmi Business Card for a Beauty, based on the website identity and colors (https://www.glowmi-example.com).
Glowmi is a beauty tech startup that gathers helpful product info for beauty lovers and consumers (such as availability on stores, price range and product reviews) for makeup products. The card design must be young, colorful but clean, and very modern.

Target Market(s)

woman, 15-35

Industry/Entity Type

Cosmetics

Contact Information for Business Card

Full Name, address, phone

Font styles to use
Other font styles liked:
• Advent Pro

Colors
e34297
86cfc6
ffffff
5c5c5c
e8e8e8
e667a6
b2b2b2

Requirements
Must have
• One full colored side with a creative design and another with card info
• Use Color palette: #95C5C5 and/or #D38AA5
• Use fonts: Advent Pro
• Use website identity: https://www.glowmi-example.com
Nice to have
• If needed extra font: Roboto

```html
<!DOCTYPE html>
<html lang="en">
<head>
<meta charset="utf-8">
<title>Glowmi Business Card</title>
<link href="https://fonts.googleapis.com/css2?family=Advent+Pro:wght@300;400;500&display=swap" rel="stylesheet">
<style>
  :root {
    --teal: #86cfc6;
    --teal-deep: #6aaea6;
    --white: #ffffff;
    --paper: #f4f5f5;
    --ink: #5c5c5c;
    --backdrop: #70787b;
  }
  * { box-sizing: border-box; margin: 0; padding: 0; }
  html, body { width: 1200px; height: 803px; overflow: hidden; }
  body {
    background: var(--backdrop);
    font-family: "Advent Pro", sans-serif;
    position: relative;
  }
  .card {
    position: absolute;
    top: 145px;
    width: 300px;
    height: 512px;
  }
  .card-front {
    left: 268px;
    background: linear-gradient(160deg, #8ad3ca 0%, var(--teal) 40%, var(--teal-deep) 100%);
    display: flex;
    flex-direction: column;
    align-items: center;
    padding-top: 165px;
  }
  .brand-circle {
    width: 100px;
    height: 100px;
    border: 3px solid rgba(255,255,255,0.9);
    border-radius: 50%;
  }
  .brand-name {
    margin-top: 30px;
    color: var(--white);
    font-weight: 300;
    font-size: 50px;
    letter-spacing: 9px;
    padding-left: 9px;
  }
  .card-back {
    left: 632px;
    background: linear-gradient(170deg, var(--white) 0%, var(--paper) 100%);
    text-align: center;
    color: var(--ink);
  }
  .person-name {
    margin-top: 62px;
    color: var(--teal);
    font-weight: 300;
    font-size: 44px;
    line-height: 1;
  }
  .person-role {
    margin-top: 2px;
    font-size: 18px;
    font-weight: 400;
  }
  .contact-list {
    list-style: none;
    margin: 50px 0 0 66px;
    text-align: left;
  }
  .contact-item {
    display: flex;
    align-items: center;
    height: 26px;
    margin-bottom: 17px;
    font-size: 18px;
    font-weight: 400;
  }
  .contact-icon {
    width: 26px;
    height: 26px;
    margin-right: 12px;
    flex: none;
  }
  .divider {
    display: block;
    margin: 33px auto 0;
  }
  .social-grid {
    display: grid;
    grid-template-columns: 120px 120px;
    column-gap: 0;
    row-gap: 12px;
    justify-content: center;
    margin-top: 18px;
  }
  .social-item {
    display: flex;
    flex-direction: column;
    align-items: center;
    font-size: 16px;
    font-weight: 400;
  }
  .social-dot {
    width: 25px;
    height: 25px;
    border-radius: 50%;
    background: var(--teal);
    margin-bottom: 6px;
  }
</style>
</head>
<body>
  <section class="card card-front">
    <div class="brand-circle"></div>
    <div class="brand-name">GLOWMI</div>
  </section>

  <section class="card card-back">
    <h1 class="person-name">John Doe</h1>
    <p class="person-role">Managing director</p>

    <ul class="contact-list">
      <li class="contact-item">
        <svg class="contact-icon" viewBox="0 0 26 26" aria-hidden="true">
          <circle cx="13" cy="13" r="13" fill="var(--teal)"/>
          <path d="M9 7c1 0 2 2.5 2 3s-1 1-1 1.6c.6 1.6 2 3 3.6 3.6.6 0 1-1 1.6-1s3 1 3 2-1.4 2-2.4 2C11 18 8 15 8 9.4 8 8.4 8.4 7 9 7z" fill="var(--white)"/>
        </svg>
        555-555-555
      </li>
      <li class="contact-item">
        <svg class="contact-icon" viewBox="0 0 26 26" aria-hidden="true">
          <circle cx="13" cy="13" r="13" fill="var(--teal)"/>
          <rect x="7" y="9" width="12" height="9" fill="var(--white)"/>
          <path d="M7 9l6 5 6-5" fill="none" stroke="var(--teal)" stroke-width="1.3"/>
        </svg>
        name@glowmi-example.com
      </li>
      <li class="contact-item">
        <svg class="contact-icon" viewBox="0 0 26 26" aria-hidden="true">
          <circle cx="13" cy="13" r="13" fill="var(--teal)"/>
          <g fill="none" stroke="var(--white)" stroke-width="1.2">
            <circle cx="13" cy="13" r="7"/>
            <ellipse cx="13" cy="13" rx="3" ry="7"/>
            <path d="M6 13h14M7 9.5h12M7 16.5h12"/>
          </g>
        </svg>
        www.glowmi-example.com
      </li>
    </ul>

    <svg class="divider" width="270" height="12" viewBox="0 0 270 12" aria-hidden="true">
      <line x1="0" y1="6" x2="126" y2="6" stroke="var(--teal)" stroke-width="2"/>
      <line x1="144" y1="6" x2="270" y2="6" stroke="var(--teal)" stroke-width="2"/>
      <circle cx="135" cy="6" r="4.5" fill="var(--teal)"/>
    </svg>

    <div class="social-grid">
      <div class="social-item"><span class="social-dot"></span>glowmi-example.com</div>
      <div class="social-item"><span class="social-dot"></span>Miss Glowmi</div>
      <div class="social-item"><span class="social-dot"></span>glowmi.</div>
      <div class="social-item"><span class="social-dot"></span>missglowmi</div>
    </div>
  </section>
</body>
</html>
```